The dental corner of brindlewood web page

website for dental office
Already have domain, mostly information only with address, telephone and google map and hours of operation on top. mobile friendly. SEO a most.

Target Market(s)

Local families

Industry/Entity Type

Dental Clinic

Number of Pages Required

1 page

Font styles to use
Serif

Colors

Designer to choose colors to be used in the design.

Requirements
Must have
• SEO
• Information to find the location
• mobile friendly
• dr's. biography
• services offered
• contect to social media (google, facebook, and instagram)
• Se habla espaƱol
• All insurance accepted
• request an appointment form to notify us

```html
<!DOCTYPE html>
<html lang="en">
<head>
<meta charset="utf-8">
<title>The Dental Corner of Brindlewood</title>
<meta name="viewport" content="width=1200">
<link rel="stylesheet" href="https://fonts.googleapis.com/css2?family=Libre+Baskerville:wght@400;700&family=Jost:wght@400;500;600;700&display=swap">
<style>
:root{
  --blue:#1a56a8;
  --blue-dark:#0f4a96;
  --green:#8cc63f;
  --ink:#111;
  --text:#666;
  --grey-bar:#b9b9b9;
  --rule:#dcdcdc;
  --footer:#1e1e1e;
  --white:#fff;
}
*{box-sizing:border-box;margin:0;padding:0}
html,body{width:1200px;height:2387px;overflow:hidden;background:var(--white)}
body{position:relative;font-family:"Jost",Arial,sans-serif;color:var(--text)}
.abs{position:absolute}
.serif{font-family:"Libre Baskerville",Georgia,serif}

/* header */
.topbar{left:0;top:0;width:1200px;height:64px;background:var(--white)}
.brand{left:161px;top:10px;display:flex;align-items:center;gap:10px}
.brand-dot{width:40px;height:40px;border-radius:50%;background:var(--blue)}
.brand-name{font-family:"Libre Baskerville",Georgia,serif;font-weight:700;color:var(--blue-dark);font-size:16px;line-height:19px;width:250px}
.top-divider{top:0;width:1px;height:64px;background:var(--rule)}
.top-link{top:24px;font-size:11.5px;font-weight:600;text-transform:uppercase;color:var(--ink)}
.top-link.accent{color:var(--blue-dark)}
.navbar{left:0;top:64px;width:1200px;height:36px;background:var(--grey-bar)}
.nav-item{top:64px;height:36px;line-height:36px;font-size:11px;font-weight:500;color:var(--white);text-transform:uppercase}
.nav-item.active{background:var(--blue);text-align:center;width:81px;left:161px;border-top:2px solid var(--blue-dark)}
.spanish{left:872px;top:64px;width:166px;height:36px;background:var(--blue);color:var(--white);font-size:11px;font-weight:700;display:flex;align-items:center;justify-content:center;gap:6px}
.spanish i{width:14px;height:14px;border-radius:50%;background:#e4a21a;display:block}

/* hero */
.hero{left:0;top:100px;width:1200px;height:494px;overflow:hidden}
.hero-photo{position:absolute;inset:0;background:linear-gradient(90deg,#c9d3dc,#e8e2dc 60%,#b8aea5)}
.hero-blue{position:absolute;inset:0;background:linear-gradient(120deg,#2b6fc0,#1d5eaf);clip-path:polygon(0 0,843px 0,780px 494px,0 494px)}
.hero-title{left:161px;top:200px;font-size:52px;font-weight:700;color:var(--white);letter-spacing:.5px}
.hero-sub{left:161px;top:280px;font-size:13px;font-weight:600;color:var(--white);text-transform:uppercase}
.field{background:var(--white);font-size:10.5px;color:#999;padding:9px 10px}
.btn-book{left:161px;top:489px;width:186px;height:31px;background:var(--blue-dark);border-bottom:2px solid var(--green);color:var(--white);font-size:11px;font-weight:700;text-transform:uppercase;display:flex;align-items:center;justify-content:center;box-shadow:0 2px 4px rgba(0,0,0,.2)}

/* shared */
.label{height:37px;padding:0 10px;background:var(--blue);border-bottom:3px solid var(--blue-dark);color:var(--white);font-size:15px;font-weight:700;line-height:36px;text-transform:uppercase}
.h2{font-family:"Libre Baskerville",Georgia,serif;font-weight:700;color:var(--ink);font-size:22px}
.para{font-size:12.5px;line-height:18.5px;color:#8a8a8a}

/* about */
.watermark{left:150px;top:640px;font-family:"Jost",Arial,sans-serif;font-weight:600;font-size:290px;line-height:1;color:#f2f2f2;white-space:nowrap;letter-spacing:4px}
.learn{left:161px;top:880px;display:flex;align-items:center;gap:10px;font-size:11.5px;font-weight:600;color:var(--ink)}
.learn span{width:24px;height:24px;border-radius:50%;background:var(--ink);display:flex;align-items:center;justify-content:center}
.rule{left:161px;top:1006px;width:1039px;height:1px;background:var(--rule)}

/* services */
.service{width:200px}
.service svg{display:block}
.service h3{margin-top:14px;font-size:12px;font-weight:700;color:var(--ink)}
.service p{margin-top:6px;font-size:12px;line-height:17px;color:#8a8a8a}
.more{display:inline-block;margin-top:14px;width:64px;height:30px;line-height:30px;text-align:center;background:var(--ink);color:var(--white);font-size:10.5px;font-weight:700}
.more.blue{background:var(--blue)}

/* bio */
.bio{left:0;top:1370px;width:1200px;height:419px;overflow:hidden}
.bio-room{position:absolute;inset:0;background:linear-gradient(110deg,#4f4f4f,#6b6866 55%,#7b7470)}
.bio-portrait{position:absolute;inset:0;background:linear-gradient(180deg,#ece9e6,#d9d4cf);clip-path:polygon(839px 0,1200px 0,1200px 419px,748px 419px)}
.bio-name{left:161px;top:1508px;color:var(--white);font-size:22px}
.bio-text{left:161px;top:1543px;width:540px;color:#e6e6e6;font-size:12.5px;line-height:18.5px}
.btn-green{left:161px;top:1692px;width:67px;height:29px;background:var(--green);color:var(--white);font-size:10.5px;font-weight:700;line-height:29px;text-align:center}

/* contact */
.contact-row{left:161px;display:flex;gap:12px;font-size:12px;line-height:16px;color:#777}
.contact-row svg{flex:none}
.map{left:689px;top:1857px;width:511px;height:284px;background:linear-gradient(135deg,#e6e6e6,#d6d6d6)}
.dotted{left:0;top:2196px;width:1200px;border-top:2px dotted #d0d0d0}
.news-title{left:161px;top:2233px;font-size:16px;font-weight:700;color:var(--ink)}
.news-input{left:582px;top:2225px;width:343px;height:36px;border:1px solid #e2e2e2;font-size:11px;color:#888;padding:11px 16px}
.btn-signup{left:942px;top:2225px;width:96px;height:36px;background:var(--green);color:var(--white);font-size:12px;font-weight:700;line-height:36px;text-align:center}

/* footer */
.footer{left:0;top:2292px;width:1200px;height:48px;background:var(--footer)}
.foot-links{left:161px;top:2306px;font-size:10.5px;color:#bbb;word-spacing:2px}
.social{top:2303px;width:26px;height:26px;border:1.5px solid var(--white);border-radius:50%}
.copyright{left:161px;top:2357px;font-size:10.5px;color:#333}
.legal{left:868px;top:2357px;font-size:10.5px;color:#333}
</style>
</head>
<body>

<header>
  <div class="abs topbar"></div>
  <div class="abs brand">
    <div class="brand-dot"></div>
    <div class="brand-name">The Dental Corner<br>of Brindlewood</div>
  </div>
  <div class="abs top-divider" style="left:559px"></div>
  <div class="abs top-divider" style="left:923px"></div>
  <div class="abs top-link accent" style="left:587px">Book an appointment</div>
  <div class="abs top-link" style="left:750px">All insurance accepted</div>
  <svg class="abs" style="left:953px;top:23px" width="17" height="17" viewBox="0 0 17 17"><circle cx="7" cy="7" r="5.5" fill="none" stroke="#111" stroke-width="2"/><line x1="11" y1="11" x2="16" y2="16" stroke="#111" stroke-width="2"/></svg>
  <svg class="abs" style="left:996px;top:22px" width="16" height="18" viewBox="0 0 16 18"><circle cx="8" cy="5" r="4" fill="none" stroke="#111" stroke-width="1.6"/><path d="M1 17c0-4 3-6 7-6s7 2 7 6" fill="none" stroke="#111" stroke-width="1.6"/></svg>

  <nav>
    <div class="abs navbar"></div>
    <div class="abs nav-item active">Home</div>
    <div class="abs nav-item" style="left:267px">About us</div>
    <div class="abs nav-item" style="left:350px">Services</div>
    <div class="abs nav-item" style="left:433px">Appointment</div>
    <div class="abs nav-item" style="left:540px">Contact us</div>
    <div class="abs spanish"><i></i>SE HABLA ESPAÑOL</div>
  </nav>
</header>

<section class="abs hero">
  <div class="hero-photo" role="img" aria-label="Photo of a dentist treating a smiling patient in the dental chair"></div>
  <div class="hero-blue"></div>
</section>
<h1 class="abs hero-title serif">THE DENTAL CORNER</h1>
<div class="abs hero-sub">Book your appointment here</div>
<form>
  <div class="abs field" style="left:161px;top:309px;width:240px;height:35px">Name</div>
  <div class="abs field" style="left:412px;top:309px;width:239px;height:35px">Phone</div>
  <div class="abs field" style="left:161px;top:355px;width:240px;height:35px">First Name</div>
  <div class="abs field" style="left:412px;top:355px;width:239px;height:35px">Booking Date</div>
  <div class="abs field" style="left:161px;top:401px;width:490px;height:72px">Email</div>
  <div class="abs btn-book">Book your appointment</div>
</form>

<section>
  <div class="abs watermark">Dental</div>
  <div class="abs label" style="left:161px;top:662px">About dental corner</div>
  <h2 class="abs h2" style="left:161px;top:727px">The Dental Corner</h2>
  <p class="abs para" style="left:161px;top:763px;width:800px">Lorem ipsum dolor sit amet, consectetur adipiscing elit, sed do eiusmod tempor incididunt ut labore et dolore magna aliqua.</p>
  <p class="abs para" style="left:161px;top:799px;width:800px">Ut enim ad minim veniam, quis nostrud exercitation ullamco laboris nisi ut aliquip ex ea commodo consequat. Duis aute irure dolor in reprehenderit in voluptate velit esse cillum dolore eu fugiat nulla pariatur. Excepteur sint occaecat cupidatat non proident, sunt in culpa qui officia deserunt mollit anim id est laborum.</p>
  <div class="abs learn"><span><svg width="8" height="10" viewBox="0 0 8 10"><path d="M1 1l6 4-6 4z" fill="#fff"/></svg></span>Learn more</div>
  <div class="abs rule"></div>
</section>

<section>
  <div class="abs label" style="left:161px;top:1066px">Our services</div>
  <div class="abs service" style="left:161px;top:1133px">
    <svg width="50" height="50" viewBox="0 0 50 50"><circle cx="25" cy="25" r="23" fill="none" stroke="#1a56a8" stroke-width="2"/><path d="M17 18c0-3 3-4 5-3l3 1 3-1c2-1 5 0 5 3 0 4-2 6-2 10s-1 7-2 7-2-6-4-6-3 6-4 6-2-3-2-7-2-6-2-10z" fill="none" stroke="#1a56a8" stroke-width="1.8"/></svg>
    <h3>Dental Service - 1</h3>
    <p>Ut enim ad minim veniam,<br>quis nostrud exercitation...</p>
    <span class="more blue">MORE</span>
  </div>
  <div class="abs service" style="left:371px;top:1133px">
    <svg width="50" height="50" viewBox="0 0 50 50"><circle cx="25" cy="25" r="23" fill="none" stroke="#999" stroke-width="2"/><path d="M17 18c0-3 3-4 5-3l3 1 3-1c2-1 5 0 5 3 0 4-2 6-2 10s-1 7-2 7-2-6-4-6-3 6-4 6-2-3-2-7-2-6-2-10z" fill="none" stroke="#999" stroke-width="1.8"/></svg>
    <h3>Dental Service - 2</h3>
    <p>sed do eiusmod tempor incid-<br>idunt ut labore et dolore...</p>
    <span class="more">MORE</span>
  </div>
  <div class="abs service" style="left:592px;top:1133px">
    <svg width="50" height="50" viewBox="0 0 50 50"><circle cx="25" cy="25" r="23" fill="none" stroke="#999" stroke-width="2"/><path d="M17 18c0-3 3-4 5-3l3 1 3-1c2-1 5 0 5 3 0 4-2 6-2 10s-1 7-2 7-2-6-4-6-3 6-4 6-2-3-2-7-2-6-2-10z" fill="none" stroke="#999" stroke-width="1.8"/></svg>
    <h3>Dental Service - 3</h3>
    <p>Lorem ipsum dolor sit amet,<br>consectetur adipiscing elit</p>
    <span class="more">MORE</span>
  </div>
  <div class="abs service" style="left:810px;top:1133px">
    <svg width="50" height="50" viewBox="0 0 50 50"><circle cx="25" cy="25" r="23" fill="none" stroke="#999" stroke-width="2"/><path d="M17 18c0-3 3-4 5-3l3 1 3-1c2-1 5 0 5 3 0 4-2 6-2 10s-1 7-2 7-2-6-4-6-3 6-4 6-2-3-2-7-2-6-2-10z" fill="none" stroke="#999" stroke-width="1.8"/></svg>
    <h3>Dental Service - 4</h3>
    <p>Duis aute irure dolor in repreh-<br>enderit in voluptate velit esse cillum</p>
    <span class="more">MORE</span>
  </div>
</section>

<section>
  <div class="abs bio">
    <div class="bio-room" role="img" aria-label="Photo of a dental treatment room, darkened"></div>
    <div class="bio-portrait" role="img" aria-label="Portrait of the dentist in a white coat"></div>
  </div>
  <div class="abs label" style="left:161px;top:1445px">Dr's bio</div>
  <h2 class="abs h2 bio-name">Dr. Marisol Elena Vidal Ortega, DDS</h2>
  <div class="abs bio-text">
    <p>Lorem ipsum dolor sit amet, consectetur adipiscing elit, sed do eiusmod tempor incididunt ut labore et dolore magna aliqua. Ut enim ad minim veniam, quis nostrud exercitation ullamco laboris nisi ut aliquip ex ea commodo consequat. Duis aute irure dolor in reprehenderit in voluptate velit esse cillum dolore eu fugiat nulla pariatur.</p>
    <p style="margin-top:18px">Excepteur sint occaecat cupidatat non proident, sunt in culpa qui officia deserunt mollit anim id est laborum.</p>
  </div>
  <div class="abs btn-green">MORE</div>
</section>

<section>
  <div class="abs label" style="left:161px;top:1860px">Contact details</div>
  <h2 class="abs h2" style="left:161px;top:1925px">The Dental Corner Contact Details</h2>
  <div class="abs contact-row" style="top:1988px">
    <svg width="24" height="24" viewBox="0 0 24 24"><circle cx="12" cy="12" r="12" fill="#111"/><path d="M12 5a4 4 0 0 0-4 4c0 3 4 9 4 9s4-6 4-9a4 4 0 0 0-4-4z" fill="#fff"/><circle cx="12" cy="9" r="1.5" fill="#111"/></svg>
    <span>4120 Harlow Ave, #208 Brindlewood,<br>FL 33890</span>
  </div>
  <div class="abs contact-row" style="top:2034px;align-items:center">
    <svg width="24" height="24" viewBox="0 0 24 24"><circle cx="12" cy="12" r="12" fill="#e8e8e8"/><path d="M8 7l2-1 2 3-1.5 1.2c.6 1.4 1.6 2.4 3 3L14.8 12l3 2-1 2c-4 0-8.8-4.8-8.8-9z" fill="#555"/></svg>
    <span>Telephone:+00 555 014 22</span>
  </div>
  <div class="abs contact-row" style="top:2071px;align-items:center">
    <svg width="24" height="24" viewBox="0 0 24 24"><circle cx="12" cy="12" r="12" fill="#e8e8e8"/><rect x="6" y="8" width="12" height="8" fill="none" stroke="#555" stroke-width="1.4"/><path d="M6 8l6 5 6-5" fill="none" stroke="#555" stroke-width="1.4"/></svg>
    <span>Email: info@dentalcornerbrindlewood.com</span>
  </div>
  <div class="abs map" role="img" aria-label="Map showing the clinic location"></div>
  <svg class="abs" style="left:946px;top:1964px" width="30" height="42" viewBox="0 0 30 42"><path d="M15 2C8 2 2 7 2 15c0 10 13 25 13 25s13-15 13-25C28 7 22 2 15 2z" fill="#fff" stroke="#e53935" stroke-width="2"/><circle cx="15" cy="15" r="4" fill="#e53935"/></svg>
</section>

<section>
  <div class="abs dotted"></div>
  <div class="abs news-title serif">The Dental Corner Newsletter Subscribe Here :</div>
  <div class="abs news-input">Enter your email id</div>
  <div class="abs btn-signup">SIGN UP</div>
</section>

<footer>
  <div class="abs footer"></div>
  <div class="abs foot-links">Home &nbsp;/&nbsp; About Us &nbsp;/&nbsp; Services &nbsp;/&nbsp; Book An Appointment &nbsp;/&nbsp; All Insurance Accept &nbsp;/&nbsp; Contact Us</div>
  <div class="abs social" style="left:920px"></div>
  <div class="abs social" style="left:951px"></div>
  <div class="abs social" style="left:982px"></div>
  <div class="abs social" style="left:1013px"></div>
  <div class="abs copyright">© Copyright 2018 The Dental Corner. All Rights Reserved</div>
  <div class="abs legal">Privacy Policy &nbsp;/&nbsp; Terms of Service</div>
</footer>

</body>
</html>
```